Geschäftspapiere für Fliesenleger - Meisterbetrieb
Zielgruppe
Wir sind ein mittelständischer Fliesenleger - Meisterbetrieb und möchten unsere Geschäftspapiere erneuern. Unsere Kunden sind Privatkunden, Gewerbetreibende sowie Öffentliche Auftraggeber.
Aufgabenstellung
Unser Logo stellen wir Ihnen zur verfügung und soll unverändert bleiben.
Wir benötigen folgende Geschäftspapiere:
- Briefpapier DIN A4
- Notizblock Karriert DIN A4
- Visitenkarten 5,5 x 8,5 cm
- Kuvert DIN lang mit Fenster
- Kuvert DIN C4 mit Fenster
Bei der Farbe Rot handelt es sich um Verkehrsrot RAL 3020
Als Schriftart haben wir uns Helvetica Neue vorgestellt.
Wir bitten jedoch auch um Vorschläge anderer Moderner und gut lesbarer Schriftarten die für Print und Web bestens geeignet sind.
Wir wünschen uns ein Modernes und Schnörkelloses Design. Bei den Dateien habe ich Ihnen ein Stockphoto angehängt um Ihnen zu zeigen wie wir uns ein Cover oder eine Broschüre vorstellen können. Nur um Ihnen unsere Ideen / Vorstellungen näher zu bringen.

```html
<!DOCTYPE html>
<html lang="de">
<head>
<meta charset="utf-8">
<title>Kerla-Fliesen – Geschäftspapiere</title>
<link href="https://fonts.googleapis.com/css2?family=Jost:wght@400;500;700&display=swap" rel="stylesheet">
<style>
  :root {
    --backdrop: #e9eaec;
    --paper: #f2f2f2;
    --brand-red: #d71a21;
    --ink: #2b2b2b;
    --ink-soft: #555555;
    --window-grey: #bdbdbd;
    --fold-grey: #e4e4e4;
  }
  * { box-sizing: border-box; margin: 0; padding: 0; }
  html, body { width: 1200px; height: 1200px; overflow: hidden; }
  body {
    position: relative;
    background: var(--backdrop);
    font-family: "Jost", "Helvetica Neue", Arial, sans-serif;
    color: var(--ink);
  }
  .sheet { position: absolute; overflow: hidden; }

  .wordmark {
    font-family: "Jost", "Helvetica Neue", Arial, sans-serif;
    font-weight: 700;
    color: var(--ink);
    white-space: nowrap;
    letter-spacing: -0.01em;
    line-height: 1;
  }
  .wordmark--light { color: #ffffff; }

  /* Letterhead */
  .letterhead {
    left: 144px; top: 102px; width: 390px; height: 549px;
    background: var(--paper);
  }
  .letterhead .wordmark { position: absolute; left: 42px; top: 46px; font-size: 16px; }
  .letterhead__body { position: absolute; left: 42px; top: 207px; width: 306px; }
  .letterhead__subject { font-size: 10.5px; font-weight: 700; margin-bottom: 26px; }
  .letterhead__body p {
    font-size: 7.4px; line-height: 1.55; color: var(--ink-soft);
    text-align: justify; margin-bottom: 9px;
  }

  /* Folder */
  .folder {
    left: 612px; top: 102px; width: 412px; height: 549px;
    background: var(--brand-red);
  }
  .folder__spine {
    position: absolute; top: 0; bottom: 0; width: 2px;
    background: rgba(0,0,0,0.12);
  }
  .folder .wordmark { position: absolute; right: 30px; bottom: 34px; font-size: 22px; }

  /* Open envelope (back) */
  .envelope-back {
    left: 144px; top: 705px; width: 359px; height: 177px;
    background: var(--paper);
  }
  .envelope-back svg { display: block; }

  /* DL envelope front */
  .envelope-dl {
    left: 148px; top: 916px; width: 354px; height: 177px;
    background: var(--paper);
  }
  .envelope-dl .wordmark { position: absolute; left: 22px; top: 72px; font-size: 15px; }
  .window {
    position: absolute; background: var(--window-grey); border-radius: 3px;
    width: 88px; height: 35px;
  }
  .envelope-dl .window { left: 236px; top: 59px; }

  /* C4 envelope */
  .envelope-c4 {
    left: 543px; top: 705px; width: 279px; height: 389px;
    background: var(--paper);
  }
  .envelope-c4 .wordmark { position: absolute; left: 21px; top: 73px; font-size: 15px; }
  .envelope-c4 .window { left: 156px; top: 55px; }

  /* Business cards */
  .card { width: 258px; height: 147px; }
  .card--front { left: 841px; top: 720px; background: var(--paper); }
  .card__details { position: absolute; left: 28px; top: 22px; font-size: 8.5px; line-height: 1.45; color: var(--ink-soft); }
  .card__name { font-weight: 700; color: var(--ink); font-size: 9.5px; letter-spacing: 0.04em; }
  .card__role { color: var(--brand-red); letter-spacing: 0.06em; margin-bottom: 10px; }
  .card__address { margin-bottom: 10px; }
  .card--front .wordmark { position: absolute; right: 12px; bottom: 14px; font-size: 13px; }
  .card--back { left: 841px; top: 931px; background: var(--brand-red); }
  .card--back .wordmark {
    position: absolute; left: 0; right: 0; top: 68px;
    text-align: center; font-size: 21px;
  }
</style>
</head>
<body>

  <section class="sheet letterhead" aria-label="Briefpapier">
    <div class="wordmark">Kerla-Fliesen</div>
    <div class="letterhead__body">
      <h2 class="letterhead__subject">Lorem ipsum dolor sit amet</h2>
      <p>Lorem ipsum dolor sit amet, mensandit urbanitas prodesset ad pro. Ex pri stet eleifend constituto, causae consetetur qui ea. Qui minimum ullamcorper ex, et nulla esse id, ne labore eripuit pro.</p>
      <p>Ei duo vivendum comprehensam. Qui paulo sitit eu, has adipisci tractatos et. Sed causae verear instructior ex, eam oblique mandamus ad. Nusquam iudicabit usu at.</p>
      <p>Ex nam oblique civibus potentium, ex nam eius assentior. Ut argumentum efficiantur has, scripta vulputate et eos. In summo oblique eum, consetetur definitionem eos te. Vel id natum officiis accusata, id vis quot veritus. Vel ne deserunt salutandi.</p>
      <p>Has cu tota civibus urbanitas. Duo ei iudico accommodare philosophia. Eu diam brute est. Cum an debet constituam, te brute essent repudiare pri, an nam reque iriure recusabo. Sit nam quis saepe persius, mea nobis legendo pertinax ei. Atqui recteque cotidieque pro ad. Ad veri everti pri.</p>
    </div>
  </section>

  <section class="sheet folder" aria-label="Mappe">
    <span class="folder__spine" style="left:6px"></span>
    <span class="folder__spine" style="left:14px"></span>
    <span class="folder__spine" style="left:22px"></span>
    <div class="wordmark wordmark--light">Kerla-Fliesen</div>
  </section>

  <section class="sheet envelope-back" aria-label="Kuvert Rückseite">
    <svg width="359" height="177" viewBox="0 0 359 177">
      <path d="M0 0 L150 150 Q179 170 208 150 L359 0 Z" fill="var(--fold-grey)"/>
      <path d="M0 0 H359 L215 64 Q179 80 143 64 Z" fill="var(--brand-red)"/>
    </svg>
  </section>

  <section class="sheet envelope-dl" aria-label="Kuvert DIN lang">
    <div class="wordmark">Kerla-Fliesen</div>
    <div class="window"></div>
  </section>

  <section class="sheet envelope-c4" aria-label="Kuvert DIN C4">
    <div class="wordmark">Kerla-Fliesen</div>
    <div class="window"></div>
  </section>

  <section class="sheet card card--front" aria-label="Visitenkarte Vorderseite">
    <div class="card__details">
      <div class="card__name">JONAS REHLBECK</div>
      <div class="card__role">MANAGER</div>
      <div class="card__address">Address Line Example<br>Street, Pl. AB/2</div>
      <div>(012) 345 678 90<br>kontakt@kerla-fliesen.de<br>www.kerla-fliesen.de</div>
    </div>
    <div class="wordmark">Kerla-Fliesen</div>
  </section>

  <section class="sheet card card--back" aria-label="Visitenkarte Rückseite">
    <div class="wordmark wordmark--light">Kerla-Fliesen</div>
  </section>

</body>
</html>
```